Energy Supplement Company Needs Packaging Design! See Your Design In Stores Everywhere!

Have you ever dreamed of seeing your designs on store shelves, billboards and in the hands of celebrities and professional athletes?

Well, your dreams may just come true… You now have the chance to have your design on the product packaging of the next major energy supplement company!

BRISKLO Vigor, Inc. is inviting the most creative, ambitious and talented designers to create a new look and feel for our brand's most popular products, the BRISKLO Vigor Tablets.

BRISKLO Vigor, Inc. began in 1985 by creating the original energy tablet, most recognized for its iconic blue packet featured in over 20,000 retail stores today. The company grew through their grass roots philosophy of distribution and quickly expanded across the United States through dozens of regional and national chains like 4-22, Marlow Q and PVD. In February of 2001, the founder of BriskLo passed and the company’s grass roots approach lost momentum and distribution as the fierce competition from energy shots and drinks hit the space that they once owned.

Theodore Lasko, a 26 year user of BRISKLO tablets, noticed that his favorite daily energy product was becoming increasingly more difficult to find in stores. As an active, serial entrepreneur with numerous ventures, his deep passion for BRISKLO led him to explore the opportunity to get involved with the company (get involved is an understatement). On August 1st of 2012, Theo raised capital and bought the company.

To increase awareness and spread his passion for BRISKLO, Mr. Lasko organized and structured the new BRISKLO Vigor, Inc. by bringing on a talented Team and investors, including Rex Palmore, a renowned sports agent/owner of the largest basketball agency whose clients include some of the biggest names in the sport. The amazing quality of our products coupled with the loyal following from the masses has led the brand to new heights and sponsorship opportunities with major sports teams and athletic organizations.

Now that the future is looking UP, we are looking for a brand refresh to bring our tablets current.

Your mission -should you chose to accept- is to develop a new graphic design for our energy tablet packets. We expect the graphic design to be modern, sleek and appealing to an 18-34 demographic. This new design will serve as the vehicle to spark excitement about energy tablets and their superiority over other forms of energy supplements. However, most importantly, you must make the package eye catching yet trusting and approachable. Keep in mind that this is something you would see in a retail store and feel comfortable reaching for and trying.

It is important to stress the mainstream direction of our company. The current packaging is somewhat 'dated' and may be out of touch with mainstream interests. Just like your aunt still rocking shoulder pads and leg warmers, we need to leave the 1980s and join everyone in 2013. Although we will begin positioning our brand towards mainstream sports, our goal is to have our products everywhere from the sidelines of major sporting events to board meetings of fortune 500 companies to the backpacks of college students. Therefore, the winning design will be one that transcends the interests of a specific group and appeals to the broader audience. Remember this is something you could see Darnell Voss, Otto Frame, and your mother holding.

Here's the great part: We are leaving all of the designing up to you!

You can redesign everything and anything you want (change colors, company logo design, content, etc.). Think of it as a blank canvas.

If you have any questions regarding design or BRISKLO Vigor, Inc. in general, please feel free to email us at design@brisk-lo.example or check out our website at www.brisk-lo.example.

Good luck!

Hi Everyone! 

Thank you to everyone who has submitted designs! Seeing what you all have come up with is exciting and impressive. However, we want to address a few commonly asked questions as well as a few general comments we have overall. 

To start, we'll better explain what we want to see in the designs. 

Although we are an energy company, we are looking to be very contemporary and sleek. Our current brand and packaging is bright and colorful, but that doesn't necessarily fit with the repositioning of our brand as a mainstream energy brand. Designs should try to only include a few colors at most. Each tablet packet should look great one their own and amazing together. 

Moreover, the designs should be relatively minimalistic. We aren't looking for anything to be "in your face". We need to reintroduce to the 18-34 generation that taking energy tablets are safe, effective, and a superior way of consuming energy supplements. Therefore, an approachable packet design is imperative. Neon colors, electricity, etc. only makes the product look scary and intimidating. 

To sum up:
Ø Use only a few colors
Ø Target an 18-34 year old demographic
Ø Minimalistic/approachable design
Ø Move away from Retro look with bright colors

FAQs:
1) We have been asked about whether or not you should be redesigning the logo on the packaging also. The answer is YES. We want every part of the packets updated. You are also designing 3 different packets or our whole energy tablet line (Surge Mix, Summit Mix, and Botanic Mix). 

2) The packets have a height of 4'' and a width of 3''. They are double-sided, so if you have a creative way of designing the back panel with the supplement facts, we would love to see it. 

We want all of you to know that we appreciate all of your hard work on creating these designs and helping to rebrand our company. Again, if you have any questions at all, the best way to reach us is by emailing us at design@brisk-lo.example. 

THANK YOU!!

The BRISKLO Design Team

Reason: We are extending the deadline for designs until Friday April 26th. We hope this will give designers a chance to submit final designs for the competition. As always, please feel free to email us directly at design@brisk-lo.example if you have any questions.

Hi everyone!

Just to let you all know, the design contest ends at 1:37am on Saturday, April 27th. We didn't want to mislead any of you by saying the contest ends tomorrow since you only have an hour and a half to submit any designs after 12am tonight. Therefore, we suggest you submit any designs you want considered by tonight. 

Thanks and good luck! 

The BRISKLO Design Team

Target Market(s)

18-34 year olds. Active, mainstream audience (not extreme-sports fans)

Requirements
Must have
• Product packet is 4''x3''
Should not have
• -Pictures of sports equipment.
-Resemble other energy products
-Look scary or intimidating
-Should not look like a cartoon or animation
-No neon colors

```html
<!DOCTYPE html>
<html lang="en">
<head>
<meta charset="utf-8">
<title>BRISKLO Vigor Tablets – Surge Mix labels</title>
<link rel="stylesheet" href="https://fonts.googleapis.com/css2?family=Josefin+Sans:wght@300;400&family=Montserrat:wght@400;700;800&display=swap">
<style>
  :root {
    --backdrop: #e8e9eb;
    --label: #ffffff;
    --ink: #2a2a2a;
    --ink-soft: #6b6b6b;
    --lime: #b7d32a;
    --lime-text: #7aa518;
    --crimson: #e0203c;
    --crimson-text: #e0203c;
    --sun: #f2e22a;
    --sun-text: #d8c400;
  }
  * { box-sizing: border-box; margin: 0; padding: 0; }
  html, body { width: 1200px; height: 900px; overflow: hidden; }
  body {
    background: var(--backdrop);
    font-family: "Montserrat", sans-serif;
    color: var(--ink);
  }
  .lineup {
    position: relative;
    width: 1200px;
    height: 900px;
  }
  .label {
    position: absolute;
    top: 230px;
    width: 330px;
    height: 440px;
    background: var(--label);
    border-radius: 6px;
    box-shadow: 0 2px 10px rgba(0,0,0,0.08);
    overflow: hidden;
  }
  .label--lime { left: 60px; --accent: var(--lime); --accent-text: var(--lime-text); }
  .label--crimson { left: 435px; --accent: var(--crimson); --accent-text: var(--crimson-text); }
  .label--sun { left: 810px; --accent: var(--sun); --accent-text: var(--sun-text); }

  .label__swoosh { position: absolute; inset: 0; width: 100%; height: 100%; }
  .label__swoosh path { fill: var(--accent); }

  .tagline {
    position: absolute; top: 44px; left: 0; right: 0;
    text-align: center;
    font-family: "Josefin Sans", sans-serif;
    font-weight: 300;
    font-size: 15px;
    letter-spacing: 3px;
    color: var(--ink-soft);
  }
  .category {
    position: absolute; top: 66px; left: 0; right: 0;
    text-align: center;
    font-family: "Josefin Sans", sans-serif;
    font-weight: 400;
    font-size: 22px;
    letter-spacing: 1px;
  }
  .brand-name {
    position: absolute; top: 100px; left: 0; right: 0;
    text-align: center;
    font-family: "Josefin Sans", sans-serif;
    font-weight: 300;
    font-size: 60px;
    letter-spacing: 2px;
    color: var(--ink);
  }
  .ingredients {
    position: absolute; top: 190px; left: 0; right: 0;
    text-align: center;
    font-family: "Josefin Sans", sans-serif;
    font-size: 15px;
    letter-spacing: 1px;
    color: var(--ink-soft);
  }
  .blend-name {
    position: absolute; top: 214px; left: 0; right: 0;
    text-align: center;
    font-weight: 800;
    font-size: 19px;
    letter-spacing: 1.5px;
    color: var(--accent-text);
  }
  .blend-contents {
    position: absolute; top: 242px; left: 0; right: 0;
    text-align: center;
    font-size: 11px;
    line-height: 1.4;
    color: var(--ink-soft);
  }
  .feature-marks {
    position: absolute; top: 258px; left: 14px;
    display: flex; flex-direction: column; gap: 8px;
  }
  .feature-marks span {
    width: 20px; height: 20px;
    background: var(--label);
    border: 1px solid rgba(0,0,0,0.15);
    border-radius: 4px;
  }
  .count {
    position: absolute; top: 318px; right: 38px;
    text-align: center;
    font-size: 18px;
    font-weight: 400;
    line-height: 1;
  }
  .count small { display: block; font-size: 7px; letter-spacing: 1px; margin-top: 2px; }
  .supplement-note {
    position: absolute; bottom: 20px; left: 16px;
    font-weight: 700;
    font-size: 13px;
    letter-spacing: 1px;
    color: var(--ink);
  }
</style>
</head>
<body>
<main class="lineup">

  <section class="label label--lime">
    <svg class="label__swoosh" viewBox="0 0 330 440" preserveAspectRatio="none" aria-hidden="true">
      <path d="M0 230 C 90 320, 220 375, 330 392 L330 440 L0 440 Z"/>
    </svg>
    <p class="tagline">FAST · BALANCED · LASTING</p>
    <p class="category">ENERGY</p>
    <h2 class="brand-name">BRISKLO</h2>
    <p class="ingredients">CoQ10 · GINSENG · GINKGO</p>
    <p class="blend-name">SURGE MIX</p>
    <p class="blend-contents">Minerals, Amino Acids<br>Enzymes, B-vitamins<br>Antioxidants</p>
    <div class="feature-marks"><span></span><span></span><span></span></div>
    <p class="count">30<small>TABLETS</small></p>
    <p class="supplement-note">DIETARY SUPPLEMENT</p>
  </section>

  <section class="label label--crimson">
    <svg class="label__swoosh" viewBox="0 0 330 440" preserveAspectRatio="none" aria-hidden="true">
      <path d="M0 230 C 90 320, 220 375, 330 392 L330 440 L0 440 Z"/>
    </svg>
    <p class="tagline">FAST · BALANCED · LASTING</p>
    <p class="category">ENERGY</p>
    <h2 class="brand-name">BRISKLO</h2>
    <p class="ingredients">CoQ10 · GINSENG · GINKGO</p>
    <p class="blend-name">SURGE MIX</p>
    <p class="blend-contents">Minerals, Amino Acids<br>Enzymes, B-vitamins<br>Antioxidants</p>
    <div class="feature-marks"><span></span><span></span><span></span></div>
    <p class="count">30<small>TABLETS</small></p>
    <p class="supplement-note">DIETARY SUPPLEMENT</p>
  </section>

  <section class="label label--sun">
    <svg class="label__swoosh" viewBox="0 0 330 440" preserveAspectRatio="none" aria-hidden="true">
      <path d="M0 230 C 90 320, 220 375, 330 392 L330 440 L0 440 Z"/>
    </svg>
    <p class="tagline">FAST · BALANCED · LASTING</p>
    <p class="category">ENERGY</p>
    <h2 class="brand-name">BRISKLO</h2>
    <p class="ingredients">CoQ10 · GINSENG · GINKGO</p>
    <p class="blend-name">SURGE MIX</p>
    <p class="blend-contents">Minerals, Amino Acids<br>Enzymes, B-vitamins<br>Antioxidants</p>
    <div class="feature-marks"><span></span><span></span><span></span></div>
    <p class="count">30<small>TABLETS</small></p>
    <p class="supplement-note">DIETARY SUPPLEMENT</p>
  </section>

</main>
</body>
</html>
```